Video Company Business Card Design

We are looking for a new design for business cards that will complement our new logo and new website design.

Target Market(s)

professionals who need video work done

Industry/Entity Type

Business

Requirements
Must have
• Logo
compliment website look seen here...http://k7pixelworks.example/brightlane/

info for card:
Dana Whitlow
Producer/ Cinematographer

532 Pellingham NE
Grand Rapids, MI 49504
(inside The RAVN Hall)
(616) 555-0142
Dana@brightlanemedia.example
www.brightlanemedia.example

```html
<!DOCTYPE html>
<html lang="en">
<head>
<meta charset="utf-8">
<title>Brightlane Media — Business Card</title>
<link href="https://fonts.googleapis.com/css2?family=Montserrat:wght@700&family=Open+Sans:wght@400;600&display=swap" rel="stylesheet">
<style>
  :root{
    --page:#2a2a2a;
    --card:#0b0b0b;
    --card-edge:#1d1d1d;
    --frame:#8fe0ad;
    --brand:#3fbf55;
    --ink:#f2f2f2;
    --ink-soft:#bdbdbd;
  }
  *{margin:0;padding:0;box-sizing:border-box}
  html,body{width:1200px;height:942px;overflow:hidden;background:var(--page)}
  .sheet{position:relative;width:1200px;height:942px}
  .card{
    position:absolute;left:250px;width:700px;height:400px;
    background:radial-gradient(ellipse at 40% 30%, #1a1a1a 0%, var(--card) 70%);
    border:4px solid var(--card-edge);
    box-shadow:0 10px 30px rgba(0,0,0,.5);
  }
  .card--front{top:47px}
  .card--back{top:495px}
  .card__frame{position:absolute;inset:12px;border:2px solid var(--frame)}
  .brand{
    position:absolute;display:flex;align-items:center;gap:14px;
    font-family:"Montserrat",sans-serif;font-weight:700;color:var(--brand);
    letter-spacing:-1px;
  }
  .brand__mark{background:var(--brand)}
  .card--front .brand{left:0;right:0;top:170px;justify-content:center;font-size:64px}
  .card--front .brand__mark{width:48px;height:48px}
  .card--back .brand{right:70px;top:62px;font-size:42px}
  .card--back .brand__mark{width:32px;height:32px}
  .person{position:absolute;left:60px;width:420px;top:152px;text-align:center;font-family:"Open Sans",sans-serif}
  .person__name{font-size:30px;color:var(--ink);font-weight:400;white-space:nowrap}
  .person__role{font-size:13px;color:var(--ink-soft);margin-top:4px}
  .address{position:absolute;right:50px;top:160px;text-align:right;font-family:"Open Sans",sans-serif;font-style:normal;color:var(--ink);font-size:16px;line-height:1.35;white-space:nowrap}
  .address small{display:block;font-size:12px;color:var(--ink-soft)}
  .contacts{position:absolute;left:40px;bottom:36px;list-style:none;font-family:"Open Sans",sans-serif;color:var(--ink);font-size:15px}
  .contacts li{display:flex;align-items:center;gap:12px;margin-top:12px}
  .contacts svg{width:24px;height:24px;flex:none}
</style>
</head>
<body>
<main class="sheet">
  <section class="card card--front" aria-label="Card front">
    <div class="card__frame"></div>
    <div class="brand"><span>BRIGHTLANE</span><span class="brand__mark"></span></div>
  </section>

  <section class="card card--back" aria-label="Card back">
    <div class="card__frame"></div>
    <div class="brand"><span>BRIGHTLANE</span><span class="brand__mark"></span></div>
    <div class="person">
      <p class="person__name">Dana Whitlow</p>
      <p class="person__role">Producer | Cinematographer</p>
    </div>
    <address class="address">
      532 Pellingham NE<br>Lakemont OR 97311
      <small>(inside The RAVN Hall)</small>
    </address>
    <ul class="contacts">
      <li>
        <svg viewBox="0 0 24 24" aria-hidden="true"><circle cx="12" cy="12" r="11" fill="#3fbf55"/><path d="M8.5 6.5l2 2-1.2 1.6c.8 1.7 2 2.9 3.6 3.6l1.6-1.2 2 2-1.5 1.8c-3.8-.4-7.3-3.9-7.7-7.7z" fill="#0b0b0b"/></svg>
        <span>(616) 555-0142</span>
      </li>
      <li>
        <svg viewBox="0 0 24 24" aria-hidden="true"><circle cx="12" cy="12" r="11" fill="#3fbf55"/><rect x="6" y="8" width="12" height="8" fill="none" stroke="#0b0b0b" stroke-width="1.5"/><path d="M6 8l6 5 6-5" fill="none" stroke="#0b0b0b" stroke-width="1.5"/></svg>
        <span>Dana@brightlanemedia.example</span>
      </li>
      <li>
        <svg viewBox="0 0 24 24" aria-hidden="true"><circle cx="12" cy="12" r="11" fill="#3fbf55"/><circle cx="12" cy="12" r="6" fill="none" stroke="#0b0b0b" stroke-width="1.4"/><ellipse cx="12" cy="12" rx="2.6" ry="6" fill="none" stroke="#0b0b0b" stroke-width="1.2"/><path d="M6 12h12" stroke="#0b0b0b" stroke-width="1.2"/></svg>
        <span>www.brightlanemedia.example</span>
      </li>
    </ul>
  </section>
</main>
</body>
</html>
```